Business card for Chiropractic clinics needs reworked / redesigned

The business card in attachment was designed 10 years ago. It is in need of an update.
We have 2 clinics:
VELDHOVE KLINIEK & VELDHOVE KLINIEK NOORD
Only one address needs to be on the card for doctors that only work in one clinic and two addresses need to be on the card for the doctors that work in both clinics.

Target Market(s)

patients/referrers

Industry/Entity Type

Medical

Contact Information for Business Card

Logo (in full or zoomed-in)
Clinic Name
Doctor name and title
clinic address, website, tel, email

Font styles to use
Sans Serif

Colors

Designer to choose colors to be used in the design.

Requirements
Must have
• Good contrast/readability
• We like modern minimalistic designs
• The Bcard needs to project our very high standard of proficiency/professionalism
Should not have
• Not curly
• Not to much colours

```html
<!DOCTYPE html>
<html lang="nl">
<head>
<meta charset="utf-8">
<title>Veldhove Kliniek – visitekaartje</title>
<link rel="stylesheet" href="https://fonts.googleapis.com/css2?family=Roboto:ital,wght@0,300;0,400;1,300&display=swap">
<style>
  :root {
    --green-dark: #66891d;
    --green-panel: #a5ca70;
    --text-grey: #4a4a4a;
    --paper: #ffffff;
  }
  html, body {
    margin: 0;
    padding: 0;
    overflow: hidden;
    background: var(--paper);
  }
  .card {
    position: relative;
    width: 1200px;
    height: 389px;
    overflow: hidden;
    font-family: "Roboto", Arial, sans-serif;
    background: var(--paper);
    color: var(--text-grey);
  }
  .card-front {
    position: absolute;
    left: 0; top: 0;
    width: 600px; height: 389px;
  }
  .brand-mark {
    position: absolute;
    left: 34px; top: 38px;
    margin: 0;
    font-size: 14px;
    font-weight: 400;
    letter-spacing: 2px;
    color: var(--green-dark);
  }
  .doctor {
    position: absolute;
    right: 42px; top: 38px;
    text-align: right;
  }
  .doctor-name {
    margin: 0;
    font-size: 26px;
    font-weight: 300;
    letter-spacing: 2.2px;
    line-height: 30px;
    color: var(--green-dark);
  }
  .doctor-title {
    margin: 2px 0 0;
    font-size: 20px;
    font-weight: 300;
    font-style: italic;
    line-height: 24px;
    color: var(--text-grey);
  }
  .clinic {
    position: absolute;
    margin: 0;
    font-style: normal;
    font-size: 16px;
    font-weight: 300;
    line-height: 20px;
    color: var(--text-grey);
  }
  .clinic-main { left: 42px; top: 167px; }
  .clinic-north { left: 47px; top: 269px; }
  .clinic-name {
    display: block;
    font-size: 18px;
    font-weight: 400;
    line-height: 22px;
  }
  .clinic-name .accent { color: var(--green-dark); }
  .label { color: var(--green-dark); }
  .card-back {
    position: absolute;
    left: 600px; top: 0;
    width: 600px; height: 389px;
    background: var(--green-panel);
  }
  .back-name {
    position: absolute;
    left: 0; right: 0; top: 162px;
    margin: 0;
    text-align: center;
    font-size: 32px;
    font-weight: 400;
    letter-spacing: 5px;
    line-height: 40px;
    color: var(--green-dark);
  }
  .back-square {
    position: absolute;
    left: 254px; top: 235px;
    width: 88px; height: 88px;
    border: 2px solid var(--paper);
  }
</style>
</head>
<body>
<main class="card">
  <section class="card-front">
    <p class="brand-mark">VELDHOVE</p>
    <header class="doctor">
      <h1 class="doctor-name">LAURENT VERHAEGEN D.C.</h1>
      <p class="doctor-title">Chiropractor</p>
    </header>
    <address class="clinic clinic-main">
      <span class="clinic-name">VELDHOVE <span class="accent">KLINIEK</span></span>
      Lindenlaan 148<br>
      <span class="label">t:</span> +32 (0) 9 555.01.42<br>
      www.veldhovekliniek.be
    </address>
    <address class="clinic clinic-north">
      <span class="clinic-name">VELDHOVE KLINIEK <span class="accent">NOORD</span></span>
      Molenstraat 57<br>
      <span class="label">t:</span> +32 (0) 9 555.08.19<br>
      www.veldhovenoord.be
    </address>
  </section>
  <section class="card-back">
    <p class="back-name">VELDHOVE</p>
    <div class="back-square"></div>
  </section>
</main>
</body>
</html>
```